Responsive webpage design for an exsiting layout (romain catholic church)

Example of content and layout on: [url removed, login to view]

header: "Seelsorgekreis Hollbachtal Ost" and the banners (attachement)
The mainmenu entires will be "Pastoralraum", "Däniken", "Dulliken", "Gretzenbach", "Schönenwerd", "Walterswil", "Zweckverband".
however new entries may follow.
The submenus are different (like on example page)

We need:
- new design (should not look like the other page)
- responsive design
- the colors and design should be matching for a romain catholic church (liturgical colors)
- the page should be "light" (not too much dark colors, background...)

```html
<!DOCTYPE html>
<html lang="de">
<head>
<meta charset="utf-8">
<title>Seelsorgekreis Hollbachtal Ost</title>
<link href="https://fonts.googleapis.com/css2?family=Cabin:wght@400;600&family=Arimo:wght@400;700&display=swap" rel="stylesheet">
<style>
:root{
  --brown:#8b4a2e;
  --brown-text:#a8755a;
  --dark:#3a3a3a;
  --darker:#2b2b2b;
  --footer:#444;
  --footer-bottom:#1f1f1f;
  --line:#dcdcdc;
  --text:#555;
  --muted:#888;
  --white:#fff;
}
*{box-sizing:border-box;margin:0;padding:0}
html,body{width:947px;height:1200px;overflow:hidden;background:var(--white)}
body{position:relative;font-family:"Arimo",Arial,sans-serif;color:var(--text);font-size:11px}
.abs{position:absolute}
.brand{left:13px;top:27px;font-weight:700;font-size:14px;line-height:17px;text-transform:uppercase;color:#aaa;width:200px}
.brand strong{color:#111}
.crest{top:10px;width:72px;height:87px;border:2px solid #222;border-radius:3px 3px 36px 36px}
.search-label{left:729px;top:27px;font-family:"Cabin",sans-serif;font-size:14px;color:#444}
.search{left:729px;top:53px;width:216px;height:30px;border:1px solid #bbb;background:var(--white)}
.search-btn{left:917px;top:53px;width:28px;height:30px;background:var(--brown)}
.nav{left:5px;top:105px;width:940px;height:50px;background:var(--dark);border-bottom:3px solid var(--brown)}
.nav a{position:absolute;top:0;height:47px;line-height:47px;font-family:"Cabin",sans-serif;font-size:14px;color:var(--white);text-decoration:none;white-space:nowrap}
.nav a.active{background:var(--brown);padding:0 14px;left:0}
.hero-frame{left:5px;top:156px;width:940px;height:334px;border:1px solid var(--line)}
.hero-img{left:14px;top:165px;width:636px;height:315px;background:linear-gradient(160deg,#d9d4c8 0%,#b8ab97 35%,#6e4434 60%,#3a2a22 100%)}
.hero-caption{left:14px;top:392px;width:636px;height:88px;background:rgba(0,0,0,.72);padding:18px 18px;color:var(--white)}
.hero-caption h2{font-family:"Cabin",sans-serif;font-weight:400;font-size:16px;margin-bottom:4px}
.hero-caption p{font-size:9.5px;line-height:16px}
.welcome{left:658px;top:165px;width:278px;height:316px;border:1px solid var(--line);box-shadow:0 1px 3px rgba(0,0,0,.15)}
.welcome-head{left:658px;top:165px;width:278px;height:42px;background:var(--brown);color:var(--white);font-family:"Cabin",sans-serif;font-size:16px;padding:12px 10px}
.welcome-img{left:669px;top:218px;width:255px;height:116px;background:linear-gradient(120deg,#2a2a2a,#8a8a8a 55%,#d8d8d8)}
.welcome-text{left:669px;top:350px;width:255px;font-size:9.5px;line-height:16px;color:var(--muted)}
.actions{left:669px;top:429px;width:255px;height:36px;border:1px solid #ccc;border-radius:3px;display:flex;background:linear-gradient(#fff,#eee)}
.actions span{flex:1;display:flex;align-items:center;justify-content:center;gap:5px;font-size:10px;color:#444;border-right:1px solid #ccc}
.actions span:last-child{border:0}
.rule{left:0;top:507px;width:947px;height:2px;background:var(--line)}
.notify{left:5px;top:529px;width:940px;height:59px;border:1px solid var(--line)}
.notify-tag{left:9px;top:533px;width:136px;height:51px;background:var(--darker);color:var(--white);font-family:"Cabin",sans-serif;font-size:15px;line-height:51px;padding-left:18px;clip-path:polygon(0 0,90% 0,100% 50%,90% 100%,0 100%)}
.notify-title{left:162px;top:539px;font-family:"Cabin",sans-serif;font-size:14px;color:var(--brown-text)}
.notify-sub{left:162px;top:560px;font-size:9.5px;color:#666}
.btn{top:540px;height:36px;border:1px solid #bbb;border-radius:3px;background:linear-gradient(#fff,#eaeaea);font-family:"Cabin",sans-serif;font-size:13px;color:#444;display:flex;align-items:center;justify-content:center;gap:6px}
.close{left:914px;top:549px;width:16px;height:16px;border-radius:50%;background:#999;color:var(--white);font-size:11px;line-height:16px;text-align:center}
.side-nav{left:10px;top:615px;width:240px;list-style:none}
.side-nav li{height:37.6px;border-bottom:1px solid #e5e5e5;padding:10px 0 0 16px;font-size:11px;color:#555;position:relative}
.side-nav li::before{content:"";position:absolute;left:2px;top:14px;border:3px solid transparent;border-left:4px solid #888}
.col{top:618px;width:150px}
.col h3{font-family:"Cabin",sans-serif;font-weight:600;font-size:12.5px;color:var(--brown-text);margin-bottom:7px}
.col h4{font-style:italic;font-weight:400;font-size:12.5px;color:#888;margin:0 0 16px 8px}
.col .t{font-family:"Cabin",sans-serif;font-weight:600;font-size:10px;color:var(--brown-text);margin:0 0 5px}
.col .d{font-size:9.5px;line-height:17px;color:#666;margin-bottom:14px}
.col .k{font-size:9.5px;color:#222;margin-bottom:3px}
.footer{left:0;top:907px;width:947px;height:251px;background:var(--footer)}
.footer-bottom{left:0;top:1157px;width:947px;height:43px;background:var(--footer-bottom);color:var(--white);font-size:9.5px}
.address{left:3px;top:990px;color:var(--white);font-size:9.5px;line-height:17px}
.f-title{font-family:"Cabin",sans-serif;font-size:15px;color:var(--white)}
.social{top:1098px;width:30px;height:30px;border-radius:3px}
.blog{left:240px;top:966px;width:228px;list-style:none}
.blog li{height:29px;border-bottom:1px solid #555;color:var(--white);font-size:9.5px;display:flex;justify-content:space-between;padding:5px 0 0 12px;position:relative}
.blog li::before{content:"";position:absolute;left:0;top:8px;border:3px solid transparent;border-left:4px solid #fff}
.blog li.empty::before{display:none}
.field{left:506px;width:225px;background:var(--white);border:1px solid #999;border-radius:2px;font-size:9px;color:#999;padding:5px}
.submit{left:506px;top:1098px;width:57px;height:27px;background:var(--brown);color:var(--white);font-weight:700;font-size:11px;border-radius:3px;text-align:center;line-height:27px}
</style>
</head>
<body>
<header>
  <div class="abs brand">Pastoralraum Niederamt Süd<br><strong>Seelsorgekreis Hollbachtal Ost</strong></div>
  <div class="abs crest" style="left:226px;background:#3a8fd4"></div>
  <div class="abs crest" style="left:311px;background:#f2d21c"></div>
  <div class="abs crest" style="left:394px;background:#fff"></div>
  <div class="abs crest" style="left:477px;background:#d82027"></div>
  <div class="abs crest" style="left:558px;background:#e03a3a"></div>
  <div class="abs search-label">Search Now</div>
  <div class="abs search"></div>
  <div class="abs search-btn"><svg width="28" height="30" viewBox="0 0 28 30"><circle cx="13" cy="14" r="4.5" fill="none" stroke="#fff" stroke-width="2"/><line x1="16" y1="17" x2="20" y2="21" stroke="#fff" stroke-width="2"/></svg></div>
</header>
<nav class="abs nav">
  <a class="active" href="#">Pastoralraum Niederamt Süd</a>
  <a href="#" style="left:240px">Lindenau</a>
  <a href="#" style="left:365px">Rietwil</a>
  <a href="#" style="left:445px">Hollbach</a>
  <a href="#" style="left:550px">Moosried a. A.</a>
  <a href="#" style="left:669px">Kirchgemeinde</a>
</nav>
<section>
  <div class="abs hero-frame"></div>
  <div class="abs hero-img" role="img" aria-label="Backsteinkirche mit Türmen vor bewölktem Himmel"></div>
  <div class="abs hero-caption"><h2>Herzlich willkommen...</h2><p>...in den Pfarreien Lindenhof | Sonnhalde | Talmatt | Seeblick des zukünftigen Pastoralraums Niederamt Süd und in der röm.-kath. Seelsorgekreis Hollbachtal Ost</p></div>
  <div class="abs welcome"></div>
  <div class="abs welcome-head">Herzlich willkommen...</div>
  <div class="abs welcome-img" role="img" aria-label="Betende Gemeinde im Gottesdienst"></div>
  <p class="abs welcome-text">...in den Pfarreien Lindenhof | Sonnhalde | Talmatt | Seeblick des zukünftigen Pastoralraums Niederamt Süd und in der röm.-kath. Seelsorgekreis Hollbachtal Ost</p>
  <div class="abs actions">
    <span><svg width="10" height="10" viewBox="0 0 10 10"><circle cx="5" cy="3" r="2.5" fill="#444"/><path d="M0 10a5 4 0 0 1 10 0z" fill="#444"/></svg>Join Us</span>
    <span><svg width="8" height="11" viewBox="0 0 8 11"><rect x="2" y="0" width="4" height="7" rx="2" fill="#444"/><path d="M1 5a3 3 0 0 0 6 0M4 8v3" stroke="#444" fill="none"/></svg>Sermons</span>
    <span><svg width="11" height="10" viewBox="0 0 11 10"><path d="M5.5 10L1 5.5A2.6 2.6 0 0 1 5.5 1.8A2.6 2.6 0 0 1 10 5.5z" fill="#444"/></svg>Support</span>
  </div>
</section>
<div class="abs rule"></div>
<section>
  <div class="abs notify"></div>
  <div class="abs notify-tag">Notifications</div>
  <div class="abs notify-title">Latest Sormens</div>
  <div class="abs notify-sub">Brookfield High School Baccalaureate, June 6, 6:00 PM</div>
  <div class="abs btn" style="left:694px;width:88px"><svg width="11" height="10" viewBox="0 0 11 10"><path d="M1 9V6a4.5 4.5 0 0 1 9 0v3" stroke="#444" stroke-width="1.6" fill="none"/></svg>Listen</div>
  <div class="abs btn" style="left:791px;width:114px"><svg width="11" height="11" viewBox="0 0 11 11"><path d="M5.5 0v7M2.5 4l3 3 3-3M0.5 8v2.5h10V8" stroke="#444" stroke-width="1.5" fill="none"/></svg>Download</div>
  <div class="abs close">×</div>
</section>
<main>
  <ul class="abs side-nav">
    <li>Pastoralraumprojekt</li><li>Ansprechpersonen</li><li>Stationen im Leben</li><li>Impuls - am Puls</li><li>Ökumene im Hollbachtal</li><li>Links</li><li>Kontakt</li>
  </ul>
  <div class="abs col" style="left:289px"><h3>Lindenau</h3><h4>Pfarrei Lindenhof</h4>
    <p class="t">Besichtigung Kirche Birkenhalde</p><p class="d" style="margin-left:8px">Donnerstag, 27.März, 18.30<br>katholisches Kirchgemeindehaus</p>
    <p class="t">Rückblick Jubiläumsanlässe</p><p class="d" style="margin-left:8px">Neue Rubrik unter "Aktuelles"</p>
    <p class="t" style="margin-left:22px">Pfarrei Chronik</p><p class="d" style="margin-left:8px">Neue Rubrik unter "Aktuelles"</p></div>
  <div class="abs col" style="left:447px"><h3>Rietwil</h3><h4 style="margin-left:0">Pfarrei Sonnhalde</h4>
    <p class="k">Lectio Divina</p><p class="d">Montag 10. März<br>09.00 im Pfarrsaal</p>
    <p class="k">Intensivnachmittag<br>Erstkommunion</p><p class="d">Mittwoch 19. März<br>14.00 im Pfarrsaal</p>
    <p class="k">Rosenkranz</p><p class="d">Donnerstag 20. März<br>19.30 in der Kirche</p></div>
  <div class="abs col" style="left:590px"><h3 style="margin-left:12px">Hollbach</h3><h4 style="margin-left:8px">Pfarrei Talmatt</h4>
    <p class="t">Jubiläumsjahr Hollbach</p><p class="t" style="margin:12px 0 34px 2px">Rückblick Jubiläumsanlässe<br>Hollbach</p>
    <p class="t" style="margin-left:2px">Gottesdienste und Andachten</p><p class="d" style="margin-left:8px">Versöhnungsfeiern vor Ostern<br>Palmsonntag - Ostern Hochfest</p></div>
  <div class="abs col" style="left:744px"><h3>Moosried an der Aare</h3><h4 style="margin-left:3px">Pfarrei Seeblick</h4>
    <p class="k">Aktuelles Pfarrblatt</p><p class="t" style="margin-left:6px">Pfarrblatt Nr. 12</p></div>
</main>
<footer>
  <div class="abs footer"></div>
  <div class="abs address">P.O Box 1234<br>Your City, City Name and Code 12345<br>(800) 12-34567 | Fax: (123) 345-6789<br>Email: Email@yourcompany.com</div>
  <div class="abs f-title" style="left:3px;top:1072px">Follow Us</div>
  <div class="abs social" style="left:3px;background:#4aa3d8"></div>
  <div class="abs social" style="left:38px;background:#3b5d9c"></div>
  <div class="abs social" style="left:73px;background:#34526e"></div>
  <div class="abs social" style="left:107px;background:#d0243a"></div>
  <div class="abs social" style="left:142px;background:#222;border:1px solid #777"></div>
  <div class="abs f-title" style="left:241px;top:936px">Blog Roll</div>
  <ul class="abs blog">
    <li>Monthly Sermons Sets<span>(65)</span></li><li>Weekly Service<span>(13)</span></li><li>About Pastor<span>(05)</span></li><li>Blog Admin<span>(02)</span></li><li>Videos<span>(01)</span></li><li class="empty" style="border:0"><span></span><span>(12)</span></li>
  </ul>
  <div class="abs f-title" style="left:506px;top:936px">Contact Us</div>
  <div class="abs field" style="top:963px;height:25px">Name</div>
  <div class="abs field" style="top:998px;height:25px">Email</div>
  <div class="abs field" style="top:1033px;height:54px">Message</div>
  <div class="abs submit">Submit</div>
  <div class="abs footer-bottom">
    <span class="abs" style="left:3px;top:16px">© 2012 Church</span>
    <span class="abs" style="left:106px;top:16px">All rights reserved</span>
    <span class="abs" style="left:873px;top:16px;display:flex;gap:4px;align-items:center"><svg width="12" height="12" viewBox="0 0 12 12"><circle cx="6" cy="6" r="6" fill="#ccc"/><path d="M3 7.5l3-3 3 3" stroke="#222" stroke-width="1.5" fill="none"/></svg>Back to top</span>
  </div>
</footer>
</body>
</html>
```